bright lane coaching needs snazzy business card that serves a dual purpose

business card needed for a Bright Lane Coaching company that takes people out on the road to teach them proficiency on their bike.
My business logo is attached. I have grey and aqua colours with my logo.
i really like bitumen/tarmac/ road in the design somehow but that is up to you.
I think navy blue will go well with my colours too. see how you go.

I want this card to look REALLY good.
the back of the card may be used for emergency contact details too
In case of Emergency I am:
Name:

Emergency Contact name
emergency contact Phone number:

• details that are essential are:
• logo
• Name: Marnie HOLT
• ABN: 53 916 204 871
• phone number: 0438 152 964
• facebook logo
• * ride tuition & proficiency
• * skills practice
• * maintenance 101
• * bike fitting service
• * cater for all ages & abilities
• backpage:
• logo
• skills confidence enjoyment
• some space for writing
• nothing girly. The business will already naturally attract women, it needs to appeal to both genders

```html
<!DOCTYPE html>
<html lang="en">
<head>
<meta charset="utf-8">
<title>Bright Lane Coaching – Business Card</title>
<link rel="stylesheet" href="https://fonts.googleapis.com/css2?family=Arimo:wght@400;700&display=swap">
<style>
  :root {
    --page: #efe9df;
    --teal-deep: #0b5d63;
    --teal-mid: #1f8a8a;
    --teal-glow: #4fb6ab;
    --aqua: #5cc2b2;
    --charcoal: #3a3a3a;
    --ink: #111;
    --navy: #1d3a6e;
    --paper-text: #e8f4f2;
  }
  * { box-sizing: border-box; margin: 0; padding: 0; }
  html, body {
    width: 1200px; height: 450px; overflow: hidden;
    background: var(--page);
    font-family: "Arimo", Arial, sans-serif;
  }
  .sheet { position: relative; width: 1200px; height: 450px; }

  .card {
    position: absolute; top: 83px; width: 526px; height: 300px;
    overflow: hidden;
    box-shadow: 0 2px 6px rgba(0,0,0,.25);
  }
  .card--front {
    left: 48px;
    background:
      radial-gradient(ellipse 55% 45% at 42% 18%, rgba(120,205,195,.55), transparent 70%),
      linear-gradient(180deg, var(--teal-mid) 0%, var(--teal-deep) 100%);
  }
  .card--back {
    left: 631px;
    background:
      radial-gradient(ellipse 30% 50% at 4% 52%, rgba(110,215,200,.85), transparent 70%),
      radial-gradient(ellipse 60% 40% at 60% 5%, rgba(90,185,180,.45), transparent 70%),
      linear-gradient(180deg, var(--teal-mid) 0%, var(--teal-deep) 100%);
  }

  .name-badge {
    position: absolute; left: 211px; top: 0; width: 104px; height: 104px;
    border-radius: 50%; background: var(--aqua);
    display: flex; flex-direction: column; align-items: center; justify-content: center;
    color: var(--ink); font-weight: 700; font-size: 18px; line-height: 21px;
    text-align: center;
  }

  .contact {
    position: absolute; left: 315px; top: 137px;
    color: var(--ink); font-size: 14px; line-height: 20px;
  }
  .contact .phone { display: flex; align-items: center; gap: 4px; }
  .contact svg { width: 12px; height: 12px; }
  .social-dot {
    position: absolute; left: 460px; top: 146px; width: 26px; height: 26px;
    border-radius: 50%; background: var(--navy);
  }

  .track {
    position: absolute; left: 0; width: 100%; height: 9px;
    background: repeating-linear-gradient(90deg, var(--charcoal) 0 8px, transparent 8px 11px);
  }
  .track--upper { top: 179px; }
  .track--lower { top: 281px; }
  .track--aqua {
    top: 279px;
    background: repeating-linear-gradient(90deg, var(--aqua) 0 8px, transparent 8px 11px);
  }

  .brand {
    position: absolute; color: var(--charcoal); font-weight: 700;
    white-space: nowrap;
  }
  .brand--front { left: 0; width: 100%; top: 228px; text-align: center; font-size: 30px; padding-left: 10px; }
  .brand--back { right: 26px; top: 232px; font-size: 21px; }

  .ice-title {
    position: absolute; left: 136px; top: 1px; width: 252px; height: 53px;
    background: var(--charcoal); border: 2px dashed var(--aqua);
    color: var(--aqua); font-size: 22px;
    display: flex; align-items: center; justify-content: center;
  }
  .ice-fields {
    position: absolute; left: 135px; top: 80px; width: 258px;
    color: var(--paper-text); font-size: 16px; line-height: 22px;
    list-style: none;
  }
  .ice-fields li { margin-bottom: 4px; }
  .ice-fields .line { display: block; border-bottom: 1px solid var(--paper-text); height: 20px; }
  .ice-fields .inline { display: flex; gap: 6px; align-items: flex-end; }
  .ice-fields .inline .line { flex: 1; height: 16px; }
</style>
</head>
<body>
<main class="sheet">
  <section class="card card--front" aria-label="Card front">
    <div class="name-badge"><span>Marnie</span><span>HOLT</span></div>
    <div class="contact">
      <p>ABN: 53 916 204 871</p>
      <p class="phone">
        <svg viewBox="0 0 24 24" aria-hidden="true"><path fill="#111" d="M6.6 10.8a15.1 15.1 0 0 0 6.6 6.6l2.2-2.2c.3-.3.7-.4 1-.2 1.1.4 2.3.6 3.6.6.6 0 1 .4 1 1V20c0 .6-.4 1-1 1A17 17 0 0 1 3 4c0-.6.4-1 1-1h3.5c.6 0 1 .4 1 1 0 1.3.2 2.5.6 3.6.1.3 0 .7-.2 1z"/></svg>
        0438.152.964
      </p>
    </div>
    <span class="social-dot" aria-hidden="true"></span>
    <div class="track track--upper"></div>
    <p class="brand brand--front">Bright Lane Coaching</p>
    <div class="track track--lower"></div>
  </section>

  <section class="card card--back" aria-label="Card back">
    <h2 class="ice-title">In Case of Emergency</h2>
    <ul class="ice-fields">
      <li class="inline">I am <span class="line"></span></li>
      <li>Emergency Contact Name:<span class="line"></span></li>
      <li>Emergency Contact Phone Number:<span class="line"></span></li>
    </ul>
    <p class="brand brand--back">Bright Lane Coaching</p>
    <div class="track track--aqua"></div>
  </section>
</main>
</body>
</html>
```